Business Card Design Project

We need a business card to reflect the design of our website - just so it all ties in - it has a retro feel and can be found at http://www.lunetaswingduo.com
We will need our phone 0493 215 764
Web address, and email lunetaduo@corvanet.com included
Our catch cry is "Classic Cocktail Music"
Perfect Live Music for Private & Corporate Events, Weddings and Dinner Music
Our names should be included :-
Deborah Feltham / piano & Owen Lockett / bass
I am now also including our logo so that it can be included (in part or whole) somehow in the design
My partner thinks we should include our logo in some form in the design of the card - i will attach this here for you. I will attach eps but if you prefer another format please let me know
Regards
Debbie

```html
<!DOCTYPE html>
<html lang="en">
<head>
<meta charset="utf-8">
<title>Luneta Duo – Business Card</title>
<link rel="stylesheet" href="https://fonts.googleapis.com/css2?family=Righteous&family=Didact+Gothic&family=Old+Standard+TT:wght@400&display=swap">
<style>
  :root {
    --backdrop: #2f2724;
    --cream: #f6f2e4;
    --teal: #7cc4ca;
    --teal-light: #a9d9dd;
    --teal-deep: #6aa3a8;
    --coral: #f0806a;
    --coral-dark: #d96a55;
    --ink: #3b3b3b;
    --ink-soft: #5a5a5a;
  }
  * { box-sizing: border-box; margin: 0; padding: 0; }
  html, body { width: 1200px; height: 576px; overflow: hidden; }
  body {
    background: var(--backdrop);
    position: relative;
    font-family: "Didact Gothic", sans-serif;
  }
  .card {
    position: absolute;
    top: 43px;
    width: 300px;
    height: 490px;
    overflow: hidden;
  }
  .card-back { left: 280px; background: linear-gradient(180deg, var(--teal-deep) 0%, #79b1b5 100%); }
  .card-front { left: 620px; background: var(--cream); }

  .coral-band {
    position: absolute;
    left: 0; right: 0; bottom: 0;
    height: 44px;
    background: var(--coral);
  }
  .coral-band::before {
    content: "";
    position: absolute;
    left: 0; right: 0; top: 9px;
    border-top: 1px dashed var(--coral-dark);
  }
  .card-front .coral-band { box-shadow: 0 -5px 0 #55585a; }

  /* back */
  .back-name {
    position: absolute;
    top: 190px; left: 0; right: 0;
    text-align: center;
    font-size: 34px;
    letter-spacing: 6px;
    color: #dbe9e9;
    opacity: .85;
  }
  .back-web {
    position: absolute;
    bottom: 16px; left: 0; right: 0;
    text-align: center;
    font-size: 9px;
    letter-spacing: 1px;
    color: #6b3a30;
  }

  /* front */
  .teal-edge {
    position: absolute;
    top: 0; bottom: 0; left: 0;
    width: 8px;
    background: var(--teal-light);
  }
  .brand-tab {
    position: absolute;
    top: 14px; right: 18px;
    display: flex;
    align-items: center;
    gap: 6px;
    font-size: 13px;
    letter-spacing: 2px;
    color: var(--teal);
  }
  .brand-dot {
    width: 14px; height: 14px;
    border-radius: 50%;
    background: var(--teal);
  }
  .tagline {
    position: absolute;
    top: 52px; left: 30px;
    font-family: "Righteous", sans-serif;
    font-size: 19px;
    color: var(--teal);
    letter-spacing: .5px;
  }
  .services {
    position: absolute;
    top: 80px; left: 30px; right: 16px;
    font-family: "Old Standard TT", serif;
    font-size: 12px;
    color: var(--ink-soft);
  }
  .musician {
    position: absolute;
    left: 60px;
    font-size: 17px;
    letter-spacing: 2px;
    color: var(--teal);
  }
  .musician .role {
    display: block;
    text-align: right;
    font-size: 12px;
    color: var(--coral);
    letter-spacing: 2px;
    margin-top: 1px;
  }
  .musician-piano { top: 150px; }
  .musician-bass { top: 205px; left: 90px; }

  .contacts {
    position: absolute;
    left: 30px; bottom: 62px;
    list-style: none;
    font-size: 10px;
    letter-spacing: 1px;
    color: var(--ink);
  }
  .contacts li { display: flex; align-items: center; gap: 7px; margin-top: 5px; }
  .contacts svg { width: 11px; height: 11px; flex: none; fill: var(--ink); }
</style>
</head>
<body>
  <section class="card card-back" aria-label="Card back">
    <div class="back-name">LUNETA DUO</div>
    <div class="coral-band"></div>
    <div class="back-web">www.lunetaswingduo.com</div>
  </section>

  <section class="card card-front" aria-label="Card front">
    <div class="teal-edge"></div>
    <div class="brand-tab"><span class="brand-dot"></span>LUNETA DUO</div>
    <h1 class="tagline">CLASSIC COCKTAIL MUSIC</h1>
    <p class="services">weddings, corporate and private events, dinner music</p>

    <p class="musician musician-piano">Deborah Feltham<span class="role">piano</span></p>
    <p class="musician musician-bass">Owen Lockett<span class="role">bass</span></p>

    <ul class="contacts">
      <li><svg viewBox="0 0 12 12"><path d="M6 1 L11 6 H9.5 V11 H7 V8 H5 V11 H2.5 V6 H1 Z"/></svg>12/48 Harlow Street Kelvin Grove Qld 4059 Australia</li>
      <li><svg viewBox="0 0 12 12"><path d="M3 1 L5 1 L6 4 L4.5 5 C5 7 6 8 7 8.5 L8 7 L11 8 L11 10 C11 11 10 11 9 11 C5 10.5 1.5 7 1 3 C1 2 2 1 3 1 Z"/></svg>0493 215 764</li>
      <li><svg viewBox="0 0 12 12"><rect x="1" y="1" width="10" height="10"/></svg>lunetaduo@corvanet.com</li>
      <li><svg viewBox="0 0 12 12"><path d="M1 3 H11 V10 H1 Z M1 3 L6 7 L11 3" fill="none" stroke="#3b3b3b" stroke-width="1.4"/></svg>www.lunetaswingduo.com</li>
    </ul>

    <div class="coral-band"></div>
  </section>
</body>
</html>
```